Mobile Design for app

Quill Harbor mobile design - This design is specifically for Wren42 who has already done the work based on previous canceled project and will be paid based on this projected as soon as it is approved.

***NO DESIGNS NEED TO BE SUBMITTED BY OTHER DESIGNERS FOR THIS PROJECT***

```html
<!DOCTYPE html>
<html lang="en">
<head>
<meta charset="utf-8">
<title>List of Exams</title>
<link href="https://fonts.googleapis.com/css2?family=Source+Sans+3:wght@400;500&display=swap" rel="stylesheet">
<style>
  :root {
    --teal: #6aaebb;
    --teal-line: #74b3bf;
    --band: #5a5b5d;
    --row: #f1f1f1;
    --ink: #3b3b3b;
    --white: #ffffff;
  }
  * { box-sizing: border-box; margin: 0; padding: 0; }
  html, body { width: 675px; height: 1200px; overflow: hidden; background: var(--white); }
  body { font-family: "Source Sans 3", "Source Sans Pro", sans-serif; color: var(--ink); position: relative; }

  .app-bar { position: absolute; top: 0; left: 0; width: 675px; height: 120px; background: var(--teal); color: var(--white); }
  .status-bar { position: absolute; top: 8px; left: 10px; right: 12px; height: 24px; font-size: 20px; color: #2e3f44; }
  .status-network { position: absolute; left: 0; }
  .status-time { position: absolute; left: 0; right: 0; text-align: center; }
  .status-battery { position: absolute; right: 0; }
  .menu-icon { position: absolute; left: 17px; top: 63px; }
  .screen-title { position: absolute; top: 56px; left: 0; right: 0; text-align: center; font-size: 32px; font-weight: 400; letter-spacing: 0.3px; }

  .total-band { position: absolute; top: 120px; left: 0; width: 675px; height: 68px; background: var(--band); color: var(--white); font-size: 30px; line-height: 68px; padding-left: 18px; }

  .intro { position: absolute; top: 228px; left: 0; width: 645px; text-align: center; font-size: 30px; line-height: 42px; color: var(--ink); padding-left: 0; }
  .intro-rule { position: absolute; top: 326px; left: 20px; width: 626px; height: 1px; background: var(--teal-line); }

  .exam-list { list-style: none; }
  .exam-item { position: absolute; left: 0; width: 673px; height: 118px; background: var(--row); }
  .status-dot { position: absolute; left: 42px; top: 41px; width: 42px; height: 42px; }
  .exam-title { position: absolute; left: 110px; top: 12px; font-size: 31px; color: var(--teal); white-space: nowrap; }
  .exam-rule { position: absolute; left: 110px; top: 59px; width: 470px; height: 1px; background: var(--teal-line); }
  .exam-meta { position: absolute; left: 110px; top: 66px; font-size: 30px; color: var(--ink); }
  .chevron { position: absolute; left: 604px; top: 40px; }
</style>
</head>
<body>
  <header class="app-bar">
    <div class="status-bar">
      <span class="status-network">Network</span>
      <span class="status-time">12:34 PM</span>
      <span class="status-battery">100%</span>
    </div>
    <svg class="menu-icon" width="46" height="30" viewBox="0 0 46 30" aria-hidden="true">
      <g fill="none" stroke="#ffffff" stroke-width="1.6">
        <rect x="1" y="1" width="44" height="5"/>
        <rect x="1" y="9" width="44" height="5"/>
        <rect x="1" y="17" width="44" height="5"/>
        <rect x="1" y="24" width="44" height="5"/>
      </g>
    </svg>
    <h1 class="screen-title">List of Exams</h1>
  </header>

  <div class="total-band">Total Exams 04</div>

  <p class="intro">Here you can view all your scheduled<br>exams and relevant information</p>
  <div class="intro-rule"></div>

  <ul class="exam-list">
    <li class="exam-item" style="top:403px">
      <svg class="status-dot" viewBox="0 0 42 42" aria-hidden="true"><circle cx="21" cy="21" r="19.5" fill="none" stroke="#6aaebb" stroke-width="3"/></svg>
      <span class="exam-title">Math 12, Period 03, 2013 / 2014</span>
      <span class="exam-rule"></span>
      <span class="exam-meta">24 Questions</span>
      <svg class="chevron" width="26" height="40" viewBox="0 0 26 40" aria-hidden="true"><polyline points="2,2 23,20 2,38" fill="none" stroke="#6aaebb" stroke-width="3"/></svg>
    </li>
    <li class="exam-item" style="top:532px">
      <svg class="status-dot" viewBox="0 0 42 42" aria-hidden="true"><circle cx="21" cy="21" r="19.5" fill="#6aaebb"/></svg>
      <span class="exam-title">Math 12, Period 03, 2013 / 2014</span>
      <span class="exam-rule"></span>
      <span class="exam-meta">24 Questions</span>
      <svg class="chevron" width="26" height="40" viewBox="0 0 26 40" aria-hidden="true"><polyline points="2,2 23,20 2,38" fill="none" stroke="#6aaebb" stroke-width="3"/></svg>
    </li>
    <li class="exam-item" style="top:659px">
      <svg class="status-dot" viewBox="0 0 42 42" aria-hidden="true"><circle cx="21" cy="21" r="19.5" fill="none" stroke="#6aaebb" stroke-width="3"/></svg>
      <span class="exam-title">Math 12, Period 03, 2013 / 2014</span>
      <span class="exam-rule"></span>
      <span class="exam-meta">24 Questions</span>
      <svg class="chevron" width="26" height="40" viewBox="0 0 26 40" aria-hidden="true"><polyline points="2,2 23,20 2,38" fill="none" stroke="#6aaebb" stroke-width="3"/></svg>
    </li>
    <li class="exam-item" style="top:788px">
      <svg class="status-dot" viewBox="0 0 42 42" aria-hidden="true"><circle cx="21" cy="21" r="19.5" fill="#6aaebb"/></svg>
      <span class="exam-title">Math 12, Period 03, 2013 / 2014</span>
      <span class="exam-rule"></span>
      <span class="exam-meta">24 Questions</span>
      <svg class="chevron" width="26" height="40" viewBox="0 0 26 40" aria-hidden="true"><polyline points="2,2 23,20 2,38" fill="none" stroke="#6aaebb" stroke-width="3"/></svg>
    </li>
  </ul>
</body>
</html>
```